'WILD' eye catching Business Card Design / Logo for production company / TV host / adventurer

Hi there,

We are looking for a 'WILD' and exciting logo and double sided business card for our business "Red Kettle Studios".

Corwin Baxley is an international television host, adventurer, author and inspirational public speaker.

We want to project Corwin's talents onto his business card.

We are looking for a business card design that can carry over onto letter heads, emails etc. We want a design that is 'WILD', different and exciting.

Feel free to check out Corwin's web site: www.redkettlestudios.co.nz to get a better understanding what he is about.

Please feel free to go completely 'WILD' on this project as we want something different with lots of WOW factors.

Thank you so much and we look forward to your designs.

We have a feeling that there will be many more designs in the near future.

Best regards,

the production team

We have added another task to the list.

If the winning designer can also provide us with a matching letterhead and email signature based on the same style of design as the business card.

Target Market(s)

People with passion.

Industry/Entity Type

Business

Requirements
Must have
• Red Kettle Studios
Corwin Baxley
42 Fernhill Lane
Ashbury 7388
New Zealand

Phone +64-(0)3-5027 416
Cell +64-(0)274-861 052

email: redkettlenz@mailbox-example.nz
www.redkettlestuios.co.nz
Nice to have
• A feature made out of the name 'Red Kettle Studios'.

Corwin Baxley's name reasonably obvious.

All other details (except web site) can be quite small.

```html
<!DOCTYPE html>
<html lang="en">
<head>
<meta charset="utf-8">
<title>Red Kettle Studios – Business Card</title>
<link href="https://fonts.googleapis.com/css2?family=Didact+Gothic&display=swap" rel="stylesheet">
<style>
  :root {
    --bg: #d9d6d3;
    --card-dark: #2b2321;
    --card-light: #ffffff;
    --accent-red: #b0392a;
    --text-light: #f2eeea;
    --text-muted: #cfc7c2;
    --rule: #8c827d;
  }
  * { box-sizing: border-box; margin: 0; padding: 0; }
  html, body {
    width: 1200px; height: 874px; overflow: hidden;
    background: var(--bg);
    font-family: "Didact Gothic", "Helvetica Neue", Arial, sans-serif;
  }
  .canvas {
    position: relative; width: 1200px; height: 874px;
  }
  .card {
    position: absolute; top: 282px;
    width: 540px; height: 309px;
    box-shadow: 0 8px 24px rgba(0,0,0,0.22);
    overflow: hidden;
  }
  /* Front side */
  .card-front {
    left: 40px;
    background: var(--card-dark);
  }
  .card-front .edge-strip {
    position: absolute; left: 0; right: 0; bottom: 0; height: 18px;
    background: var(--card-light);
  }
  .card-front .brand {
    position: absolute; left: 0; right: 0; top: 104px;
    text-align: center;
    color: var(--text-light);
    font-size: 46px; letter-spacing: 0.5px;
  }
  .card-front .web {
    position: absolute; left: 0; right: 0; top: 172px;
    text-align: center;
    color: var(--text-muted);
    font-size: 15px; letter-spacing: 1px;
  }
  /* Back side */
  .card-back {
    left: 620px;
    background: var(--card-light);
  }
  .card-back .brand {
    position: absolute; left: 0; right: 0; top: 26px;
    text-align: center;
    color: var(--accent-red);
    font-size: 30px;
  }
  .card-back .info-band {
    position: absolute; left: 0; right: 0; top: 86px; height: 148px;
    background: var(--card-dark);
    color: var(--text-light);
  }
  .info-band .band-rule {
    position: absolute; left: 0; right: 0; height: 1px;
    background: var(--rule);
  }
  .info-band .band-rule.top { top: 12px; }
  .info-band .band-rule.bottom { bottom: 12px; }
  .info-band .name {
    position: absolute; left: 0; right: 0; top: 20px;
    text-align: center; font-size: 22px; letter-spacing: 0.5px;
  }
  .info-band .address {
    position: absolute; left: 40px; top: 66px;
    font-size: 13px; line-height: 19px; color: var(--text-muted);
  }
  .info-band .divider {
    position: absolute; left: 236px; top: 58px; width: 1px; height: 64px;
    background: var(--rule);
  }
  .info-band .contacts {
    position: absolute; left: 252px; top: 58px;
    font-size: 12px; line-height: 19px; color: var(--text-muted);
  }
  .contacts .label { display: inline-block; width: 42px; }
  .card-back .web {
    position: absolute; left: 0; right: 0; top: 258px;
    text-align: center;
    color: var(--accent-red);
    font-size: 19px; letter-spacing: 0.5px;
  }
</style>
</head>
<body>
<main class="canvas">
  <section class="card card-front" aria-label="Business card front">
    <p class="brand">Red Kettle Studios</p>
    <p class="web">www.redkettlestudios.co.nz</p>
    <div class="edge-strip"></div>
  </section>

  <section class="card card-back" aria-label="Business card back">
    <p class="brand">Red Kettle Studios</p>
    <div class="info-band">
      <div class="band-rule top"></div>
      <p class="name">Corwin Baxley</p>
      <address class="address">
        42 Fernhill Lane<br>
        Ashbury 7388<br>
        New Zealand
      </address>
      <div class="divider"></div>
      <p class="contacts">
        <span class="label">phone</span>+64-(0)3-5027 416<br>
        <span class="label">cell</span>+64-(0)274-861 052<br>
        <span class="label">email</span>redkettlenz@mailbox-example.nz
      </p>
      <div class="band-rule bottom"></div>
    </div>
    <p class="web">www.redkettlestuios.co.nz</p>
  </section>
</main>
</body>
</html>
```